High end wine label at Austrian Winery

We are a traditional winery in Austria in region Burgenland. We are looking for a relaunch of our current wine label for our [solstice] series. It's a high end wine series at an upper price range. At the moment we have just two kinds of the label, one white one for the white wines and one black one for the red wines. This is a series of wine, white, red, sweet, sparkling and a top wine categories. So we need the same label, but in 4 different ways to distinguish the wines plus the sparkling. Maybe in color, patterns, ... or something else. The label should be very simple, including our new logo. It's also possible to make one label but we can splitting two parts of the label. The size of the label does not matter, need not be the same as now. It's a bit higher than a normal bottle. Additionally we need a back label with wine description and the wine dates on it.

Target Market(s)

private consumers and restaurants, no retailers

Colors

Designer to choose colors to be used in the design.

Requirements
Must have
• simple label with 4 different categories (red, white, sweet, top) plus Frizzante label, new logo integrated, high end label. Just logo, grape variety and [solstice] as text on the front label as text
Nice to have
• It's just good, if there'sa possibility to have different colors of each grape variety (about 10 different), but all the same style. top Wines should have an extraordinary design, but familiar with the others
Should not have
• no cheap look

```html
<!DOCTYPE html>
<html lang="en">
<head>
<meta charset="utf-8">
<title>Weber Frizzante Label</title>
<link href="https://fonts.googleapis.com/css2?family=Yellowtail&family=Montserrat:wght@400;500&family=Josefin+Sans:wght@400&family=Open+Sans:wght@700&display=swap" rel="stylesheet">
<style>
  :root {
    --page: #ffffff;
    --label-dark: #16191f;
    --label-mid: #1e222a;
    --slate: #5c6576;
    --olive: #6d8b2f;
    --silver: #b9babd;
  }
  html, body {
    margin: 0;
    width: 1200px;
    height: 1200px;
    overflow: hidden;
    background: var(--page);
  }
  .label {
    position: absolute;
    left: 389px;
    top: 40px;
    width: 422px;
    height: 1120px;
    background: linear-gradient(160deg, var(--label-mid) 0%, var(--label-dark) 55%, var(--label-mid) 100%);
    overflow: hidden;
  }
  .signature-name {
    position: absolute;
    top: 30px;
    left: 0;
    width: 100%;
    text-align: center;
    font-family: "Yellowtail", cursive;
    font-size: 54px;
    line-height: 72px;
    color: var(--olive);
  }
  .brand-mark {
    position: absolute;
    left: 80px;
    top: 106px;
    width: 258px;
    height: 258px;
  }
  .brand-mark-name {
    position: absolute;
    inset: 0;
    display: flex;
    align-items: center;
    justify-content: center;
    font-family: "Montserrat", sans-serif;
    font-weight: 500;
    font-size: 40px;
    letter-spacing: 0.12em;
    color: var(--slate);
  }
  .wordmark,
  .tagline {
    position: absolute;
    transform: rotate(-90deg);
    text-align: center;
    white-space: nowrap;
    font-family: "Montserrat", sans-serif;
    color: var(--slate);
  }
  .wordmark {
    left: -81px;
    top: 656px;
    width: 580px;
    height: 74px;
    line-height: 74px;
    font-size: 100px;
    font-weight: 500;
    letter-spacing: 0.2em;
  }
  .tagline {
    left: 22px;
    top: 664px;
    width: 503px;
    height: 36px;
    line-height: 36px;
    font-size: 30px;
    font-weight: 500;
    letter-spacing: 0.16em;
  }
  .variety {
    position: absolute;
    top: 996px;
    left: 0;
    width: 100%;
    text-align: center;
    font-family: "Josefin Sans", sans-serif;
    font-size: 46px;
    line-height: 52px;
    letter-spacing: 0.04em;
    color: var(--silver);
  }
  .series {
    position: absolute;
    top: 1062px;
    left: 0;
    width: 100%;
    text-align: center;
    font-family: "Open Sans", sans-serif;
    font-weight: 700;
    font-size: 27px;
    line-height: 34px;
    letter-spacing: 0.03em;
    color: var(--olive);
  }
  .base-band {
    position: absolute;
    left: 0;
    bottom: 0;
    width: 100%;
    height: 17px;
    background: var(--olive);
  }
</style>
</head>
<body>
  <div class="label">
    <div class="signature-name">anton Weber</div>

    <div class="brand-mark">
      <svg width="258" height="258" viewBox="0 0 258 258" aria-hidden="true">
        <circle cx="129" cy="129" r="124" fill="none" stroke="var(--slate)" stroke-width="8"/>
      </svg>
      <div class="brand-mark-name">WEBER</div>
    </div>

    <div class="wordmark">WEBER</div>
    <div class="tagline">ESTATE SINCE 1958</div>

    <div class="variety">FRIZZANTE</div>
    <div class="series">[SOLSTICE]</div>

    <div class="base-band"></div>
  </div>
</body>
</html>
```